Business Card Design Project

I need a business card for a Management Consultancy. We work with organisational design and development and strategic change using facilitation, consulting and coaching.

Size of card is 90 x 55mm.

Logo is attached.

Wording is:

Carla Brennick
Director

tel 0417286194
email is: info@bluepathvista.com.au

Target Market(s)

Government departments and not for profit organisations mainly.

Industry/Entity Type

Business

Requirements
Must have
• White or colour background not black.

On one side of the card, either back or front please include the words:

Guiding Purposeful Growth

Two sided business card

```html
<!DOCTYPE html>
<html lang="en">
<head>
<meta charset="UTF-8">
<title>BluePathVista Business Cards</title>
<link href="https://fonts.googleapis.com/css2?family=Carlito:wght@400;700&display=swap" rel="stylesheet">
<style>
  :root {
    --navy: #2b4a6b;
    --navy-dark: #2a4463;
    --navy-light: #3f6f9f;
    --green: #7dc242;
    --white: #ffffff;
    --ink: #2b3c52;
    --shadow: rgba(0, 0, 0, 0.32);
  }
  * { margin: 0; padding: 0; box-sizing: border-box; }
  html, body {
    width: 1200px;
    height: 827px;
    overflow: hidden;
    background: var(--white);
    font-family: "Carlito", Calibri, Arial, sans-serif;
  }
  .canvas { position: relative; width: 1200px; height: 827px; }

  .card {
    position: absolute;
    width: 492px;
    height: 277px;
    box-shadow: 0 4px 22px var(--shadow);
    overflow: hidden;
  }

  /* Front */
  .card-front { left: 61px; top: 304px; background: var(--white); }
  .brand {
    position: absolute;
    left: 26px;
    top: 23px;
    display: flex;
    align-items: center;
    gap: 12px;
  }
  .brand-mark {
    width: 52px;
    height: 52px;
    border-radius: 50%;
    background: var(--navy);
  }
  .brand-name {
    font-size: 27px;
    font-weight: 700;
    color: var(--navy);
    letter-spacing: -0.3px;
  }
  .name-band {
    position: absolute;
    left: 0;
    top: 112px;
    width: 100%;
    height: 78px;
    border-top: 2px solid #24384f;
    background: linear-gradient(90deg, var(--navy-dark) 0%, var(--navy-light) 50%, var(--navy-dark) 100%);
    display: flex;
    align-items: center;
    justify-content: center;
  }
  .holder-name {
    color: var(--white);
    font-size: 24px;
    font-weight: 400;
  }
  .rule {
    position: absolute;
    left: 0;
    top: 193px;
    width: 100%;
    height: 6px;
    background: var(--green);
  }
  .rule-centre {
    position: absolute;
    left: 76px;
    top: 0;
    width: 335px;
    height: 6px;
    background: var(--navy);
  }
  .contact {
    position: absolute;
    left: 37px;
    top: 220px;
    font-size: 13px;
    line-height: 17px;
    color: var(--ink);
  }
  .contact-label { color: var(--green); }

  /* Backs */
  .card-back {
    display: flex;
    align-items: center;
    justify-content: center;
  }
  .card-back-light { left: 630px; top: 128px; background: var(--white); }
  .card-back-dark { left: 628px; top: 463px; background: var(--navy); }
  .tagline {
    color: var(--green);
    font-size: 25px;
    font-weight: 400;
    margin-top: -4px;
  }
</style>
</head>
<body>
<div class="canvas">

  <section class="card card-front">
    <div class="brand">
      <div class="brand-mark"></div>
      <span class="brand-name">BluePathVista</span>
    </div>
    <div class="name-band">
      <span class="holder-name">Carla Brennick</span>
    </div>
    <div class="rule"><div class="rule-centre"></div></div>
    <div class="contact">
      <div><span class="contact-label">E-mail:</span> info@bluepathvista.com.au</div>
      <div><span class="contact-label">Phone:</span> 0417286194</div>
    </div>
  </section>

  <section class="card card-back card-back-light">
    <p class="tagline">Guiding Purposeful Growth</p>
  </section>

  <section class="card card-back card-back-dark">
    <p class="tagline">Guiding Purposeful Growth</p>
  </section>

</div>
</body>
</html>
```